Company or website name
- Comedy Juggler Website
- I am a Comedy/Technical Juggler, working for cruise lines, corporate events, and festivals around the world

```html
<!DOCTYPE html>
<html lang="en">
<head>
<meta charset="utf-8">
<title>Danny Flinger – Comedy Juggler</title>
<link href="https://fonts.googleapis.com/css2?family=Arimo:wght@400;700&display=swap" rel="stylesheet">
<style>
:root{
  --bg-deep:#03070d;
  --bg-mid:#0f2633;
  --panel:#1b2f7a;
  --panel-dark:#101c55;
  --nav:#2c44a8;
  --nav-light:#4860c4;
  --content:#2a4294;
  --content-light:#3d5ab0;
  --frame:#1c6ad8;
  --white:#ffffff;
  --soft:#e6ecff;
  --star:#e8eeff;
}
*{margin:0;padding:0;box-sizing:border-box}
html,body{width:1200px;height:879px;overflow:hidden}
body{
  font-family:"Arimo",Arial,sans-serif;
  color:var(--white);
  background:
    radial-gradient(ellipse 520px 260px at 620px 20px, rgba(140,90,200,.55), transparent 70%),
    radial-gradient(ellipse 380px 220px at 880px 40px, rgba(120,170,90,.45), transparent 70%),
    radial-gradient(ellipse 380px 220px at 330px 40px, rgba(70,90,200,.5), transparent 70%),
    radial-gradient(ellipse 700px 600px at 600px 300px, var(--bg-mid), var(--bg-deep) 80%);
  position:relative;
}
.social{position:absolute;top:56px;left:812px;display:flex;gap:14px}
.social a{display:flex;align-items:center;gap:5px;color:var(--white);text-decoration:none;font-size:14px;font-weight:700}
.social a::before{content:"";width:12px;height:12px;border-radius:50%;background:var(--white)}
.site{position:absolute;left:184px;top:103px;width:847px;height:704px;background:var(--panel)}
.top-nav{height:51px;background:linear-gradient(var(--nav-light),var(--nav));display:flex;align-items:center;justify-content:flex-end;padding-right:33px}
.nav-list{display:flex;list-style:none;font-size:19px}
.nav-list li+li::before{content:"|";margin:0 10px}
.nav-list a{color:var(--white);text-decoration:none}
.brand{position:absolute;left:-24px;top:8px;width:330px;z-index:2}
.brand-first{font-size:34px;font-weight:700;line-height:36px;color:var(--star);letter-spacing:-1px}
.brand-last{font-size:56px;font-weight:700;line-height:56px;color:var(--star);letter-spacing:-1px;padding-left:20px}
.brand-tagline{font-size:15px;font-weight:700;margin-top:6px;padding-left:30px}
.hero{position:relative;height:313px;background:linear-gradient(180deg,var(--panel) 0%,var(--panel-dark) 100%)}
.performer-photo{position:absolute;left:16px;top:80px;width:333px;height:233px;
  background:radial-gradient(ellipse at 50% 40%,#6a7fd0,#2c3f96 70%,var(--panel-dark))}
.video{position:absolute;left:389px;top:26px;width:434px;height:264px;border:3px solid var(--frame);background:#1542b8;padding:9px 10px 10px}
.video-screen{position:relative;width:100%;height:100%;
  background:radial-gradient(ellipse at 50% 40%,#3a2a22,#130d0b 70%,#050404)}
.play{position:absolute;left:50%;top:50%;transform:translate(-50%,-70%)}
.content{position:relative;height:288px;background:linear-gradient(180deg,var(--content-light),var(--content) 40%,var(--panel-dark))}
.intro{position:absolute;left:32px;top:20px;width:461px}
.intro h1{font-size:21px;letter-spacing:1px;font-weight:700;margin-bottom:9px}
.intro p{font-size:14.6px;line-height:21.5px;text-align:justify;text-indent:26px;color:var(--soft)}
.calendar{position:absolute;left:533px;top:16px}
.calendar h2{font-size:18px;font-weight:700;margin-bottom:10px}
.cal-box{width:269px;height:146px;border:2px solid rgba(255,255,255,.8);border-radius:10px;
  box-shadow:0 0 6px rgba(255,255,255,.6);background:linear-gradient(#4d6ac2,#3a56b0);padding:8px 10px}
.cal-grid{width:100%;border-collapse:collapse}
.cal-grid th{font-size:6px;font-weight:700;text-align:left;height:14px}
.cal-grid td{font-size:14px;font-weight:700;height:22px;border-bottom:1px solid rgba(255,255,255,.25);border-left:1px solid rgba(255,255,255,.2);padding-left:2px}
.cal-grid td.next{font-size:8px;font-weight:400}
.clients{position:absolute;left:29px;top:213px}
.clients h2{font-size:17px;font-weight:700}
.client-row{position:absolute;left:88px;top:244px;display:flex;align-items:center;gap:26px;list-style:none;font-size:14px;font-weight:700}
.client-row li{display:flex;align-items:center;gap:5px}
.client-row li::before{content:"";width:9px;height:9px;background:var(--white)}
.footer-nav{height:52px;background:linear-gradient(var(--nav-light),var(--nav));display:flex;align-items:center;justify-content:center}
.footer-nav .nav-list li+li::before{margin:0 6px}
.copyright{position:absolute;top:817px;left:0;width:1200px;text-align:center;font-size:14.5px}
</style>
</head>
<body>
<nav class="social">
  <a href="#">Chirp</a>
  <a href="#">Facepage</a>
</nav>

<div class="site">
  <header class="top-nav">
    <ul class="nav-list">
      <li><a href="#">Home</a></li><li><a href="#">Biography</a></li><li><a href="#">Workshows</a></li><li><a href="#">Promo Material</a></li><li><a href="#">Agents</a></li><li><a href="#">Booking Info</a></li>
    </ul>
  </header>

  <div class="brand">
    <div class="brand-first">DANNY</div>
    <div class="brand-last">FLINGER</div>
    <div class="brand-tagline">Australia's Comedy Juggling Superstar</div>
  </div>

  <section class="hero">
    <div class="performer-photo" role="img" aria-label="Performer holding two axes with a surprised pose"></div>
    <div class="video">
      <div class="video-screen" role="img" aria-label="Video of the juggler performing on a stage">
        <svg class="play" width="56" height="56" viewBox="0 0 56 56">
          <circle cx="28" cy="28" r="26" fill="#2a5fd6" stroke="#bcd0ff" stroke-width="2"/>
          <path d="M22 17 L40 28 L22 39 Z" fill="#ffffff"/>
        </svg>
      </div>
    </div>
  </section>

  <section class="content">
    <article class="intro">
      <h1>A Night of Quirky Mayhem</h1>
      <p>Danny Flinger is Australia's Newest Comedy Sensation. At the tender age of 23, Danny Flinger is one of Australia's most sought after entertainers. A 45 minute spectacular of belly laughs, stupid dancing, useless skills, and contorted ideas add up to a great fun show for all! A 45 minute spectacular of belly laughs, stupid dancing, useless skills, and contorted ideas add up to a great fun show for all!</p>
    </article>

    <aside class="calendar">
      <h2>Calender</h2>
      <div class="cal-box">
        <table class="cal-grid">
          <tr><th>Sunday</th><th>Monday</th><th>Tuesday</th><th>Wednesday</th><th>Thursday</th><th>Friday</th><th>Saturday</th></tr>
          <tr><td>1</td><td>2</td><td>3</td><td>4</td><td>5</td><td>6</td><td>7</td></tr>
          <tr><td>8</td><td>9</td><td>10</td><td>11</td><td>12</td><td>13</td><td>14</td></tr>
          <tr><td>15</td><td>16</td><td>17</td><td>18</td><td>19</td><td>20</td><td>21</td></tr>
          <tr><td>22</td><td>23</td><td>24</td><td>25</td><td>26</td><td>27</td><td>28</td></tr>
          <tr><td>29</td><td>30</td><td>31</td><td class="next">1</td><td class="next">2</td><td class="next">3</td><td class="next">4</td></tr>
        </table>
      </div>
    </aside>

    <div class="clients"><h2>Clients</h2></div>
    <ul class="client-row">
      <li>Harbourline</li><li>Pantry Co</li><li>Golden Bun</li><li>Kestrel Motors</li><li>Vantor</li><li>Lumera</li>
    </ul>
  </section>

  <footer class="footer-nav">
    <ul class="nav-list">
      <li><a href="#">Home</a></li><li><a href="#">Biography</a></li><li><a href="#">Workhows</a></li><li><a href="#">Promo Material</a></li><li><a href="#">Agents</a></li><li><a href="#">Booking Info</a></li>
    </ul>
  </footer>
</div>

<p class="copyright">Copyrights@www.dannyflinger.com</p>
</body>
</html>
```